Discreet simple classy for adult entertainment

I would like a matte black business card with gold writing for my business. Keeping it simple. Having my following:

Lana frost
Events. Entertainment. Promotions
0491726580

or alternatively could have what i had on my previous card below but i think i prefer the above as again - discretion.

Maybe a nice gold line thru the card or some other very simple design . Or not open to ideas/ can be doublesided if any good ideas with that.

included pics of my old bus card. not sure weather i want a photo on it or not. if i do it wont be the same pic. i kinda wanted a card that was discreet so if it was in someones wallet they wouldn't neccessarily realise it was from a stripper.

Target Market(s)

men

Industry/Entity Type

Business

Contact Information for Business Card

Lana frost
0491726580

Requirements
Nice to have
• i don't know i am really open to anything. im giving my cards to guys so something they can have in their wallet that is discreet preferably.

```html
<!DOCTYPE html>
<html lang="en">
<head>
<meta charset="utf-8">
<title>Lana Frost — Business Card</title>
<link rel="stylesheet" href="https://fonts.googleapis.com/css2?family=Fira+Sans:wght@300;600&display=swap">
<style>
  :root {
    --page-bg: #e9eaeb;
    --card-black: #232325;
    --name-white: #e4e4e4;
    --text-light: #e8e8e8;
    --accent-orange: #e07b24;
  }
  html, body {
    margin: 0;
    width: 1200px;
    height: 900px;
    overflow: hidden;
    background: var(--page-bg);
  }
  .business-card {
    position: absolute;
    left: 150px;
    top: 246px;
    width: 900px;
    height: 408px;
    background: var(--card-black);
    font-family: "Fira Sans", Arial, sans-serif;
    overflow: hidden;
  }
  .contact-name {
    position: absolute;
    left: 72px;
    top: 98px;
    margin: 0;
    font-size: 60px;
    font-weight: 600;
    line-height: 1;
    color: var(--name-white);
    letter-spacing: 0.2px;
  }
  .contact-phone {
    position: absolute;
    left: 72px;
    top: 180px;
    margin: 0;
    font-size: 34px;
    font-weight: 300;
    line-height: 1;
    color: var(--text-light);
  }
  .services {
    position: absolute;
    left: 0;
    top: 347px;
    width: 100%;
    height: 0;
  }
  .service-rule {
    position: absolute;
    top: -1.5px;
    height: 3px;
    background: var(--accent-orange);
  }
  .service-label {
    position: absolute;
    top: -20px;
    font-size: 33px;
    font-weight: 300;
    line-height: 1;
    color: var(--text-light);
    white-space: nowrap;
  }
</style>
</head>
<body>
  <div class="business-card">
    <h1 class="contact-name">Lana Frost</h1>
    <p class="contact-phone">049 172 6580</p>
    <div class="services">
      <span class="service-rule" style="left:0;width:52px"></span>
      <span class="service-label" style="left:74px">Promotions</span>
      <span class="service-rule" style="left:272px;width:86px"></span>
      <span class="service-label" style="left:377px">Events</span>
      <span class="service-rule" style="left:502px;width:86px"></span>
      <span class="service-label" style="left:608px">Entertainment</span>
      <span class="service-rule" style="left:846px;width:54px"></span>
    </div>
  </div>
</body>
</html>
```